Ad design for a macarons brand

We are a dessert brand with one product line: macarons. Our products delight. Every bite is a dream!

We are launching a new product and would like to lunch a small tactical campaign for the product to boost sales.

The new macron is mango ganache and the middle a mix of sour mango and yuzu (https://www.plumvarell.com/about-the-fruit-584302).

Here are some images we took of the new macaron
https://www.fennlocker.com/sh/qrtwpzhkvbmls/AAFJtRWD-nxPlkhQZ7CeW4DLp?dl=0

I attach the brand guideline document.

Required sizes

1080 x 1350
1080 x 1920

```html
<!DOCTYPE html>
<html lang="en">
<head>
<meta charset="utf-8">
<title>Mango Ganache Macaron Campaign — Ad Sizes</title>
<link rel="stylesheet" href="https://fonts.googleapis.com/css2?family=Instrument+Serif&display=swap">
<style>
  :root {
    --board: #262626;
    --label: #8a8a8a;
    --swirl-orange: #ff7a0a;
    --swirl-deep: #f25c05;
    --swirl-yellow: #ffd400;
    --sun: #ffe000;
    --sun-warm: #ffc81e;
    --badge: #ffc414;
    --ink-light: #ffffff;
    --ink-orange: #f0650f;
  }
  * { margin: 0; padding: 0; box-sizing: border-box; }
  html, body { width: 1200px; height: 1200px; overflow: hidden; background: var(--board); }
  body { position: relative; font-family: "Instrument Serif", Georgia, serif; }

  .size-label {
    position: absolute;
    transform: translateX(-50%);
    color: var(--label);
    font-size: 33px;
    line-height: 1;
    white-space: nowrap;
  }
  .size-label--portrait { left: 317px; top: 748px; }
  .size-label--story { left: 889px; top: 170px; }

  .ad {
    position: absolute;
    width: 519px;
    overflow: hidden;
  }
  .ad--portrait { left: 58px; top: 70px; height: 648px; }
  .ad--story { left: 630px; top: 225px; height: 921px; }

  .ad__swirl {
    position: absolute; inset: 0;
    background:
      radial-gradient(ellipse 40% 25% at 85% 10%, var(--swirl-yellow) 0%, transparent 70%),
      radial-gradient(ellipse 35% 30% at 10% 70%, var(--swirl-yellow) 0%, transparent 70%),
      radial-gradient(ellipse 45% 30% at 90% 75%, #ffb000 0%, transparent 70%),
      radial-gradient(ellipse 50% 40% at 60% 35%, var(--swirl-deep) 0%, transparent 75%),
      linear-gradient(160deg, var(--swirl-orange), #ff9a10 55%, var(--swirl-orange));
  }

  .ad__headline {
    position: absolute; left: 0; right: 0;
    text-align: center;
    color: var(--ink-light);
    font-weight: 400;
    text-transform: uppercase;
    letter-spacing: -0.01em;
    white-space: nowrap;
  }
  .ad--portrait .ad__headline { top: 34px; font-size: 44px; line-height: 34px; }
  .ad--story .ad__headline { top: 53px; font-size: 54px; line-height: 40px; }
  .ad--story .ad__headline span { display: block; }
  .ad--story .ad__headline .gap { margin-top: 19px; }

  .disc { position: absolute; border-radius: 50%; }
  .disc--flavour { background: var(--sun); display: flex; align-items: center; justify-content: center; }
  .disc--brand { background: var(--badge); display: flex; align-items: center; justify-content: center; }

  .product-photo {
    position: absolute;
    border-radius: 50%;
    background: radial-gradient(circle at 50% 40%, var(--sun) 0%, var(--sun) 45%, var(--sun-warm) 100%);
  }
  .ad--portrait .product-photo { left: 74px; top: 155px; width: 371px; height: 371px; }
  .ad--story .product-photo { left: 54px; top: 323px; width: 412px; height: 412px; }

  .ad--portrait .disc--flavour { left: 59px; top: 463px; width: 150px; height: 150px; }
  .ad--portrait .disc--brand { left: 358px; top: 495px; width: 124px; height: 124px; }
  .ad--story .disc--flavour { left: 37px; top: 663px; width: 166px; height: 166px; }
  .ad--story .disc--brand { left: 337px; top: 742px; width: 152px; height: 152px; }

  .flavour-name {
    color: var(--ink-orange);
    text-align: center;
    font-weight: 400;
    transform: translateX(6px);
  }
  .ad--portrait .flavour-name { font-size: 30px; line-height: 24px; margin-top: -10px; }
  .ad--story .flavour-name { font-size: 34px; line-height: 27px; margin-top: -8px; }

  .brand-name {
    color: var(--ink-light);
    font-weight: 400;
    letter-spacing: 0.02em;
  }
  .ad--portrait .brand-name { font-size: 30px; }
  .ad--story .brand-name { font-size: 36px; }
</style>
</head>
<body>
  <p class="size-label size-label--portrait">1080 X 1350</p>
  <p class="size-label size-label--story">1080 X 1920</p>

  <section class="ad ad--portrait">
    <div class="ad__swirl" role="img" aria-label="Flowing marbled swirl pattern in orange and yellow"></div>
    <h1 class="ad__headline">Macarons.<br>Our products delight.<br>Every bite is a dream!</h1>
    <div class="product-photo" role="img" aria-label="Photo of mango macarons with cubed mango and green leaves on a yellow circle"></div>
    <div class="disc disc--flavour"><p class="flavour-name">mango<br>ganache</p></div>
    <div class="disc disc--brand"><p class="brand-name">MERIS</p></div>
  </section>

  <section class="ad ad--story">
    <div class="ad__swirl" role="img" aria-label="Flowing marbled swirl pattern in orange and yellow"></div>
    <h1 class="ad__headline">
      <span>Macarons.</span>
      <span class="gap">Our products</span>
      <span>delight.</span>
      <span class="gap">Every bite</span>
      <span>is a dream!</span>
    </h1>
    <div class="product-photo" role="img" aria-label="Photo of mango macarons with cubed mango and green leaves on a yellow circle"></div>
    <div class="disc disc--flavour"><p class="flavour-name">mango<br>ganache</p></div>
    <div class="disc disc--brand"><p class="brand-name">MERIS</p></div>
  </section>
</body>
</html>
```